one side yoga classes, other side rental log cabin

I need a flyer to advertise yoga classes on a lake , and to describe the various styles of classes, and who they can benefit, Days Times .prices
Linked to it is a rental log cabin that can be rented privetly to families or Groups (8 max) www.fernvalestays.com This also is rented to yoga teacher that would like to Hire Cabin and the Studio www.velinoshaven.co.uk or
for Holistic weekends.

Teacher

```html
<!DOCTYPE html>
<html lang="en">
<head>
<meta charset="utf-8">
<title>Velinos Retreat &amp; Velinos Lodge</title>
<link rel="stylesheet" href="https://fonts.googleapis.com/css2?family=Crimson+Text:wght@400;600;700&display=swap">
<style>
:root{
  --panel-dark:rgba(12,10,8,0.86);
  --panel-cream:rgba(243,234,214,0.9);
  --title-cream:#f6efe0;
  --heading-gold:#dca55c;
  --text-light:#f4efe6;
  --text-dark:#3a2b1c;
  --link-brown:#5a3a1a;
  --lodge-sky:#b9c7c2;
  --lodge-green:#5f7a3e;
  --lodge-deep:#34451f;
  --class-warm:#8a6a48;
  --class-floor:#c9a57a;
}
*{margin:0;padding:0;box-sizing:border-box}
html,body{width:847px;height:1200px;overflow:hidden;background:#fff}
.flyer{position:relative;width:847px;height:1200px;overflow:hidden;font-family:"Crimson Text",Georgia,serif}
.photo-lodge{position:absolute;left:0;top:0;width:847px;height:690px;
  background:linear-gradient(180deg,var(--lodge-sky) 0%,#9fb19a 30%,var(--lodge-green) 62%,var(--lodge-deep) 100%)}
.photo-class{position:absolute;left:0;top:690px;width:847px;height:510px;
  background:linear-gradient(180deg,#6b5a40 0%,var(--class-warm) 45%,var(--class-floor) 100%)}
.yoga-panel{position:absolute;left:0;top:0;width:470px;height:1030px;background:var(--panel-dark);
  border-radius:0 0 22px 0;padding:18px 22px 0 24px;color:var(--text-light)}
.yoga-panel h2{font-weight:700;font-size:25px;color:var(--heading-gold);line-height:1.1;margin-bottom:3px}
.yoga-panel h2.meditation{margin-top:12px}
.yoga-panel p{font-size:15.2px;line-height:19.5px;margin-bottom:15px}
.lodge-title{position:absolute;left:480px;top:22px;width:352px;height:66px;background:var(--title-cream);
  border-radius:12px 12px 0 0;display:flex;align-items:center;justify-content:center}
.lodge-title h1{font-weight:600;font-size:30px;color:var(--text-dark)}
.lodge-panel{position:absolute;left:480px;top:100px;width:352px;height:575px;background:var(--panel-cream);
  border-radius:14px;padding:16px 20px;text-align:center;color:var(--text-dark)}
.lodge-panel p{font-size:15.2px;line-height:19.5px;margin-bottom:15px}
.lodge-panel .site{font-weight:700;color:var(--link-brown)}
.contact{position:absolute;left:0;top:1030px;width:560px;height:170px;
  background:linear-gradient(90deg,rgba(12,10,8,0.8) 0%,rgba(12,10,8,0.55) 75%,rgba(12,10,8,0) 100%);
  padding:24px 24px 0;color:var(--text-light)}
.contact h3{font-weight:700;font-size:22px;line-height:1.2}
.contact p{font-size:17px;line-height:1.3}
.contact strong{font-weight:700}
</style>
</head>
<body>
<main class="flyer">
  <div class="photo-lodge" role="img" aria-label="Photograph of the log cabin lodge by the lake, surrounded by green trees"></div>
  <div class="photo-class" role="img" aria-label="Photograph of a yoga class practising together in the studio"></div>

  <section class="yoga-panel">
    <h2>Yoga</h2>
    <p>Studies show that yoga is significantly effective for improving wellbeing and resilience to stress in the workplace. A team of researchers working at Eldermoor University found that a six week programme of Solan Yoga reduced anxiety and fatigue, while increasing emotional well-being and resilience to stress. Results showed that the Solan Yoga group reported feeling significantly less anxious, unsure, confused, tired, and depressed than the control group who did not practice Solan Yoga.</p>
    <p>Velinos Retreat uses Solan Yoga in the studio and practices outside when the weather permits. It is one of the UK's most popular forms of yoga, comprising of easy-to-learn flowing movements, simple breathing techniques and effective relaxation methods.</p>
    <p>The ethos of Velinos Retreat is enlightenment and positive feelings. We have a variety of sessions held throughout the week, that allow us to provide different levels of intensity, ranging from a complete beginner lesson, learning basic movements to the more advanced.</p>
    <p>We are in a perfect position to be able to invite individuals and couples to attend for more personal sessions, taking advantage of the Spa area and Zen garden during the experience.</p>
    <h2 class="meditation">Meditation</h2>
    <p>Meditating does more than just feel good and calm you down, it makes you perform better - and alters the structure of your brain, researchers have found. People who meditate say the practice restores their energy, and some claim they need less sleep as a result. Many studies have reported that the brain works differently during meditation - brainwave patterns change and neuronal firing patterns synchronise.</p>
    <p>Meditation at Velinos Retreat takes place wherever you feel most comfortable, whether it be at the lakeside, in the studio, in the zen garden or on the gardens. The most important aspect of meditation at Velinos Retreat is for you to come away feeling the power of positive balance.</p>
    <p>Millions of people worldwide feel the benefit of meditation for personal or professional reasons.</p>
  </section>

  <header class="lodge-title"><h1>Velinos Lodge</h1></header>
  <section class="lodge-panel">
    <p>Welcome to Fernvale Stays! We are a family who rent out a cabin in the heart of the Norfolk countryside to offer people a chance to rest and relax!</p>
    <p>The cabin is surrounded by nature, with a picturesque lake and opportunities for walks through any number of the sleepy Norfolk villages.</p>
    <p>But don't worry, the cabin is still outfitted with all the modern luxuries you would expect so you can relax in comfort!</p>
    <p>With room for up to 8 people, then we offer the perfect getaway for the whole family. If you wish to see if there is availability for when you are looking to go away, then please get in touch with us here and we will help build your ideal country escape!</p>
    <p>We also offer retreats for any groups looking to really relax and enjoy a weekend of meditation and yoga in a studio suspended over the lake itself. If you wish to see the dates of our next retreat or view our weekly class schedule, then please visit our sister site <span class="site">www.velinoshaven.co.uk</span> for all of the details.</p>
  </section>

  <footer class="contact">
    <h3>Velinos Retreat</h3>
    <p>7 Marsh Lane, Wexley. QX9 4RT</p>
    <p>Email <strong>info@velinos.co.uk</strong> | Telephone 01632 960 418 | Mobile 07700 900 615</p>
  </footer>
</main>
</body>
</html>
```